Varelto Stationary and Branding Documents

Corporate Identity Branding stationary needed for IT Recruiting Firm.

I already have a Logo, business cards and website. I need to get designs completed for the remaining corporate identity documents.

The documentation should use similar colors as my website and business card. The designs should modern and clean.

http://varelto-example.com/

Target Market(s)

Information Technology Industry

Industry/Entity Type

Information Technology

Colors
3377b5
0255a3
fbee3e
f78f20
f37122
33a6d7
000000
0592cd

Requirements
Must have
• Letter Head
• Folder Design
• PowerPoint Design
• Invoice
• Envelope
Nice to have
• Proposal
• Flyer
• Brochure
Should not have
• Logo
• Business Cards
• Website

```html
<!DOCTYPE html>
<html lang="en">
<head>
<meta charset="utf-8">
<title>Varelto Letterhead</title>
<link rel="stylesheet" href="https://fonts.googleapis.com/css2?family=Open+Sans:wght@400;600&display=swap">
<style>
  :root {
    --brand-blue: #0a5596;
    --brand-grey: #5f6062;
    --brand-orange: #f37122;
    --paper: #ffffff;
    --backdrop: #e4e5e7;
    --footer-text: #ffffff;
  }
  * { margin: 0; padding: 0; box-sizing: border-box; }
  html, body {
    width: 1066px;
    height: 1200px;
    overflow: hidden;
    background: var(--backdrop);
    font-family: "Open Sans", sans-serif;
  }
  .letterhead {
    position: absolute;
    left: 133px;
    top: 34px;
    width: 800px;
    height: 1132px;
    background: var(--paper);
    overflow: hidden;
    box-shadow: 0 4px 18px rgba(0,0,0,0.12);
  }
  .brand {
    position: absolute;
    left: 118px;
    top: 92px;
    display: flex;
    align-items: center;
    gap: 10px;
  }
  .brand-name {
    font-size: 50px;
    font-weight: 400;
    color: var(--brand-blue);
    letter-spacing: 1px;
    line-height: 1;
  }
  .brand-mark {
    width: 10px;
    height: 10px;
    background: var(--brand-orange);
  }
  .footer-bands {
    position: absolute;
    left: 0;
    bottom: 0;
    width: 800px;
    height: 160px;
  }
  .footer-bands .band-grey { fill: var(--brand-grey); }
  .footer-bands .band-blue { fill: var(--brand-blue); }
  .contact {
    position: absolute;
    bottom: 20px;
    left: 462px;
    display: flex;
    gap: 16px;
    color: var(--footer-text);
    font-size: 12px;
    line-height: 16px;
  }
  .contact-address { font-style: normal; }
  .contact-line { display: flex; align-items: center; gap: 7px; }
  .contact-line svg { width: 11px; height: 11px; fill: var(--footer-text); }
</style>
</head>
<body>
  <main class="letterhead">
    <header class="brand">
      <span class="brand-name">varelto</span>
      <span class="brand-mark"></span>
    </header>

    <svg class="footer-bands" viewBox="0 0 800 160" preserveAspectRatio="none">
      <path class="band-grey" d="M0,92 L340,152 L340,160 L0,160 Z"/>
      <path class="band-blue" d="M200,160 Q500,80 800,18 L800,160 Z"/>
    </svg>

    <footer class="contact">
      <address class="contact-address">
        <div>One Harbor Plaza</div>
        <div>418 Linden Avenue NW</div>
      </address>
      <div class="contact-direct">
        <div class="contact-line">
          <svg viewBox="0 0 24 24"><path d="M6.6 10.8a15.1 15.1 0 0 0 6.6 6.6l2.2-2.2a1 1 0 0 1 1-.25 11.4 11.4 0 0 0 3.6.57 1 1 0 0 1 1 1V20a1 1 0 0 1-1 1A17 17 0 0 1 3 4a1 1 0 0 1 1-1h3.5a1 1 0 0 1 1 1c0 1.25.2 2.45.57 3.57a1 1 0 0 1-.25 1z"/></svg>
          <span>5550142876</span>
        </div>
        <div class="contact-line">
          <svg viewBox="0 0 24 24"><path d="M2 6h20v12H2z M2 6l10 7 10-7" fill="none" stroke="#fff" stroke-width="2.4"/></svg>
          <span>info@varelto-example.com</span>
        </div>
      </div>
    </footer>
  </main>
</body>
</html>
```